business card for a shoe shop

we would like a business card for a family owned shoe shop.
With this information included.
Darnell's Shoe Store
Family owned since 1947

then on other side
Darnell's Shoe Store
Footwear fitting specialist
Phone: 9187 2630
218 Quarry St, Fernleigh Downs 3187
(cnr. Hartwick Rd and Quarry St)
darnellshoes218@examplemail.com
if could incorporate the purple color on card i have attached.

```html
<!DOCTYPE html>
<html lang="en">
<head>
<meta charset="utf-8">
<title>Darnell's Shoe Store – Business Card</title>
<link rel="stylesheet" href="https://fonts.googleapis.com/css2?family=Anton&family=Poppins:wght@400;500;600&display=swap">
<style>
  :root {
    --purple: #7b2ff7;
    --purple-soft: #e4d9f7;
    --ink: #2b2b2b;
    --ink-muted: #444;
    --card: #f7f7f7;
    --page: #ffffff;
  }
  * { box-sizing: border-box; margin: 0; padding: 0; }
  html, body { width: 687px; height: 1200px; overflow: hidden; background: var(--page); }
  .canvas {
    width: 687px; height: 1200px;
    display: flex; flex-direction: column; align-items: center; justify-content: center;
    gap: 80px;
  }
  .card {
    position: relative; width: 560px; height: 320px;
    background: var(--card); overflow: hidden;
    box-shadow: 0 2px 8px rgba(0,0,0,0.12);
  }
  .monogram-block {
    position: absolute; background: var(--purple-soft);
  }

  /* Front */
  .card--front .monogram-block { left: 360px; top: 0; width: 170px; height: 302px; }
  .front-title {
    position: absolute; left: 48px; top: 112px;
    font-family: "Anton", sans-serif; font-size: 44px; line-height: 1;
    color: var(--purple); letter-spacing: 0.5px; text-transform: uppercase;
  }
  .front-tagline {
    position: absolute; left: 52px; top: 170px;
    font-family: "Poppins", sans-serif; font-weight: 500; font-size: 17px;
    color: var(--ink); letter-spacing: 2.6px; text-transform: uppercase;
  }
  .band-bottom { position: absolute; left: 0; bottom: 0; width: 100%; height: 18px; background: var(--purple); }

  /* Back */
  .band-top { position: absolute; left: 0; top: 0; width: 100%; height: 18px; background: var(--purple); }
  .card--back .monogram-block { left: 30px; top: 96px; width: 170px; height: 224px; }
  .back-title {
    position: absolute; left: 30px; top: 46px;
    font-family: "Poppins", sans-serif; font-weight: 600; font-size: 25px;
    color: var(--purple); text-transform: uppercase; letter-spacing: 0.3px;
  }
  .back-tagline {
    position: absolute; left: 30px; top: 80px;
    font-family: "Poppins", sans-serif; font-weight: 500; font-size: 16px;
    color: var(--ink); letter-spacing: 0.8px;
  }
  .rule { position: absolute; left: 0; top: 112px; width: 100%; height: 2px; background: var(--purple); }
  .contact-list {
    position: absolute; left: 260px; top: 138px; list-style: none;
    display: flex; flex-direction: column; gap: 16px;
  }
  .contact-item { display: flex; align-items: center; gap: 14px; }
  .contact-icon {
    flex: none; width: 26px; height: 26px; border-radius: 5px; background: var(--purple);
    display: flex; align-items: center; justify-content: center;
  }
  .contact-text {
    font-family: "Poppins", sans-serif; font-size: 12.5px; line-height: 1.35; color: var(--ink-muted);
  }
</style>
</head>
<body>
<main class="canvas">

  <section class="card card--front" aria-label="Card front">
    <div class="monogram-block" aria-hidden="true"></div>
    <h1 class="front-title">Darnell's Shoe Store</h1>
    <p class="front-tagline">Family owned since 1947</p>
    <div class="band-bottom"></div>
  </section>

  <section class="card card--back" aria-label="Card back">
    <div class="band-top"></div>
    <div class="monogram-block" aria-hidden="true"></div>
    <h2 class="back-title">Darnell's Shoe Store</h2>
    <p class="back-tagline">Footwear fitting specialist</p>
    <div class="rule"></div>
    <ul class="contact-list">
      <li class="contact-item">
        <span class="contact-icon">
          <svg width="14" height="14" viewBox="0 0 24 24"><path fill="#fff" d="M6.6 10.8a15.2 15.2 0 0 0 6.6 6.6l2.2-2.2c.3-.3.7-.4 1-.2 1.1.4 2.3.6 3.6.6.6 0 1 .4 1 1V20c0 .6-.4 1-1 1A17 17 0 0 1 3 4c0-.6.4-1 1-1h3.5c.6 0 1 .4 1 1 0 1.3.2 2.5.6 3.6.1.3 0 .7-.2 1z"/></svg>
        </span>
        <span class="contact-text">9187 2630</span>
      </li>
      <li class="contact-item">
        <span class="contact-icon">
          <svg width="14" height="14" viewBox="0 0 24 24"><path fill="#fff" d="M12 2a7 7 0 0 0-7 7c0 5.2 7 13 7 13s7-7.8 7-13a7 7 0 0 0-7-7zm0 9.5A2.5 2.5 0 1 1 12 6.5a2.5 2.5 0 0 1 0 5z"/></svg>
        </span>
        <span class="contact-text">218 Quarry St, Fernleigh Downs<br>3187 (cnr. Hartwick Rd and Quarry St)</span>
      </li>
      <li class="contact-item">
        <span class="contact-icon">
          <svg width="14" height="14" viewBox="0 0 24 24"><path fill="#fff" d="M3 5h18v14H3z"/><path fill="none" stroke="#7b2ff7" stroke-width="2" d="M3 6l9 7 9-7"/></svg>
        </span>
        <span class="contact-text">darnellshoes218@examplemail.com</span>
      </li>
    </ul>
  </section>

</main>
</body>
</html>
```